Profi-Kistenhof
Zielgruppe
Profi-Kistenhof.de vermietet Lagercontainern an Privatkunden und Gewerbetriebende
Vermietung von Stellfächen für Wohnmobile/Boote etc
Das ganze auf einem Gewerbegelände in Köln (Brauweiler)
Aufgabenstellung
Erstellung eines 2-Seitigen DIN lang (10,5 x 21 cm) Flyers
Seite A: Vermietung von Lagercontainern
Seite B: Stellfächen für Wohnmobile/Boote
Wichtig: Die Sicherheit (Zutrittskontrolle, Videoüberwachung, Brandmeldeanlage)
Preise sollen auf Flyern erscheinen, diese wie auch die Textee möchte ich jedoch ändern können.
Alle Texte können auch von der Seite profi-kistenhof.de übernommen werden
Das Logo (siehe boxen_welten.ai) müsste noch bearbeitet werden .... also "boxenwelten" raus und dafür "Lagerraum Container" rein
Gerne mit Symbolen arbeiten ..

```html
<!DOCTYPE html>
<html lang="de">
<head>
<meta charset="utf-8">
<title>Profi-Kistenhof Flyer</title>
<link rel="stylesheet" href="https://fonts.googleapis.com/css2?family=Noto+Sans:wght@400;700&display=swap">
<style>
  :root{
    --green:#1b6b36;
    --green-text:#1d7a3c;
    --blue:#0f69a9;
    --blue-text:#1470b0;
    --ink:#1e1e1e;
    --white:#ffffff;
    --price-green:#e5efe8;
    --price-blue:#e3eef6;
    --frame:#8a8a8a;
    --logo-bg:#1f3d78;
  }
  *{box-sizing:border-box;margin:0;padding:0}
  html,body{width:798px;height:1200px;overflow:hidden;background:var(--white)}
  body{font-family:"Noto Sans",Verdana,sans-serif;color:var(--ink);position:relative}
  .page-frame{position:absolute;left:2px;top:2px;width:794px;height:1196px;border:1px solid #c8c8c8}
  .flyer{position:absolute;left:64px;width:665px;border:1px solid var(--frame);background:var(--white)}
  .flyer--containers{top:91px;height:471px}
  .flyer--parking{top:647px;height:474px}
  .contact{position:absolute;left:30px;top:30px;font-size:15px;line-height:21px}
  .tagline{font-weight:700;margin-bottom:6px}
  .flyer--containers .tagline{color:var(--green-text)}
  .flyer--parking .tagline{color:var(--blue-text)}
  .company{font-weight:700}
  .contact dl{display:grid;grid-template-columns:58px auto}
  .brand{position:absolute;left:396px;top:24px;width:234px;height:76px;background:var(--logo-bg);
    display:flex;align-items:center;justify-content:center;gap:10px;color:var(--white);font-size:22px;font-weight:700}
  .brand-mark{width:18px;height:18px;background:var(--white)}
  .title{position:absolute;left:30px;font-size:35px;font-weight:700;line-height:1;letter-spacing:-.2px}
  .flyer--containers .title{top:160px;color:var(--green)}
  .flyer--parking .title{top:165px;color:var(--blue)}
  .band{position:absolute;left:0;right:0;bottom:0;color:var(--white)}
  .flyer--containers .band{top:210px;background:var(--green)}
  .flyer--parking .band{top:219px;background:var(--blue)}
  .intro{position:absolute;left:30px;top:18px;width:330px;font-size:15px;line-height:21px}
  .features{position:absolute;left:151px;list-style:none;font-size:15px;line-height:27px}
  .flyer--containers .features{top:98px}
  .flyer--parking .features{top:113px}
  .features li{display:flex;align-items:center;gap:9px}
  .features svg{width:11px;height:11px;flex:none}
  .price-box{position:absolute;left:406px;top:16px;width:245px;padding:12px 10px}
  .flyer--containers .price-box{height:207px;background:var(--price-green);color:var(--green-text)}
  .flyer--parking .price-box{left:403px;top:10px;height:205px;background:var(--price-blue);color:var(--blue-text)}
  .price{font-size:22px;font-weight:700;line-height:28px}
  .offer{margin-top:12px;font-size:15px;line-height:20px}
  .fineprint{margin-top:12px;font-size:8.5px;line-height:11px}
  .visual{position:absolute}
  .visual--boxes{left:22px;top:160px;width:118px;height:77px;background:linear-gradient(#f4f4f4,#d9d9d9)}
  .visual--container{left:528px;top:159px;width:110px;height:88px;background:linear-gradient(90deg,#2f4774,#4c6a9e 60%,#8a6a3c)}
  .visual--camper{left:40px;top:130px;width:97px;height:93px;background:var(--white);border-radius:8px}
</style>
</head>
<body>
<div class="page-frame"></div>

<section class="flyer flyer--containers">
  <div class="contact">
    <p class="tagline">günstig - sicher - lagern</p>
    <p class="company">Profi-Kistenhof.de</p>
    <dl><dt>Tel.:</dt><dd>02234 5550182</dd><dt>Mail:</dt><dd>mk@profi-kistenhof.de</dd></dl>
  </div>
  <div class="brand"><span class="brand-mark"></span>Profi-Kistenhof</div>
  <h1 class="title">Vermietung von Lagercontainern</h1>
  <div class="band">
    <p class="intro">Profi-Kistenhof vermietet Container zu kleinem Preis und Top-Konditonen für die Lagerung privater oder gewerblicher Güter - auch als kurzfristige Lösung (z.B. bei Umzug) geeignet.</p>
    <ul class="features">
      <li><svg viewBox="0 0 12 12"><path d="M1 6.5l3 3 7-7" fill="none" stroke="#fff" stroke-width="2"/></svg>Rund um die Uhr zugänglich</li>
      <li><svg viewBox="0 0 12 12"><path d="M1 6.5l3 3 7-7" fill="none" stroke="#fff" stroke-width="2"/></svg>14m² bzw. 33m³ Kapazität</li>
      <li><svg viewBox="0 0 12 12"><path d="M1 6.5l3 3 7-7" fill="none" stroke="#fff" stroke-width="2"/></svg>Zutrittskontrolle</li>
      <li><svg viewBox="0 0 12 12"><path d="M1 6.5l3 3 7-7" fill="none" stroke="#fff" stroke-width="2"/></svg>Videoüberwacht</li>
      <li><svg viewBox="0 0 12 12"><path d="M1 6.5l3 3 7-7" fill="none" stroke="#fff" stroke-width="2"/></svg>14 Tage Kündigungsfrist</li>
    </ul>
    <div class="visual visual--boxes" role="img" aria-label="Gestapelte Umzugskartons"></div>
    <div class="price-box">
      <p class="price">148,- € pro Monat*</p>
      <p class="offer">1 Monat gratis<br>bei einer Anmietung<br>ab 3 Monaten</p>
      <p class="fineprint">* Preis gilt pro Monat und Container für private Vermietung, bei gewerblicher Anmietung zzgl. 19% MwSt.</p>
    </div>
    <div class="visual visual--container" role="img" aria-label="Geöffneter Lagercontainer mit Kisten"></div>
  </div>
</section>

<section class="flyer flyer--parking">
  <div class="contact">
    <p class="tagline">günstig - sicher - lagern</p>
    <p class="company">Profi-Kistenhof.de</p>
    <dl><dt>Tel.:</dt><dd>02234 5550182</dd><dt>Mail:</dt><dd>mk@profi-kistenhof.de</dd></dl>
  </div>
  <div class="brand"><span class="brand-mark"></span>Profi-Kistenhof</div>
  <h1 class="title">Stellfächen für Wohnmobile/Boote</h1>
  <div class="band">
    <p class="intro">Profi-Kistenhof vermietet Stellflächen für Wohnmobile oder Boote zu kleinem Preis und Top-Konditonen - auch als kurzfristige Lösung (z.B. bei Umzug) geeignet.</p>
    <ul class="features">
      <li><svg viewBox="0 0 12 12"><path d="M1 6.5l3 3 7-7" fill="none" stroke="#fff" stroke-width="2"/></svg>Rund um die Uhr zugänglich</li>
      <li><svg viewBox="0 0 12 12"><path d="M1 6.5l3 3 7-7" fill="none" stroke="#fff" stroke-width="2"/></svg>Zutrittskontrolle</li>
      <li><svg viewBox="0 0 12 12"><path d="M1 6.5l3 3 7-7" fill="none" stroke="#fff" stroke-width="2"/></svg>Videoüberwacht</li>
      <li><svg viewBox="0 0 12 12"><path d="M1 6.5l3 3 7-7" fill="none" stroke="#fff" stroke-width="2"/></svg>Brandmeldeanlage</li>
      <li><svg viewBox="0 0 12 12"><path d="M1 6.5l3 3 7-7" fill="none" stroke="#fff" stroke-width="2"/></svg>14 Tage Kündigungsfrist</li>
    </ul>
    <div class="visual visual--camper" role="img" aria-label="Symbol Wohnmobil"></div>
    <div class="price-box">
      <p class="price">148,- € pro Monat*</p>
      <p class="offer">1 Monat gratis<br>bei einer Anmietung<br>ab 3 Monaten</p>
      <p class="fineprint">* Preis gilt pro Monat und Stellplatz<br>für private Vermietung,<br>bei gewerblicher Anmietung zzgl. 19% MwSt.</p>
    </div>
  </div>
</section>
</body>
</html>
```